Web Design Project for Weightwise Commons

Aim
As the peak body on obesity, to be the ‘go to website’ for information about obesity and for people that are overweight or obese. Whether an individual looking for support and advice; a professional such as a dietician or a medical practitioner; an academic researcher studying the field; a related organisation specialising in cancer; diabetes or cardio issues or a policy maker
Requirements
A professional site that is compatible for viewing on PCs Mac, ipads and iphones
To include the following:
• Announcements bar – (for adding in conferences, news grabs etc)
• Search tool (for academic’s papers, terms in fact sheets)
• Secure log in (for KPR & WC directors & staff personnel for board papers etc)
• Good visuals including changing photos (should be engaging for public – see sample)
• Web sharing apps Email/Friendgrid login and other social media; like button
• Get involved – to express interest in conferences; potential sponsors
• Ebulletin (KPR)- subscribe - emailed to a database or posted to a social media site
• WC Recommended Apps - LTD, KORVEL, Plattertrack? P&V
• WC blog
• Capture database of emails/enquiries for ebulletin and fact sheets
Contents
Landing page – containing aspects above (announcements, search tool, visuals, social media tools, get involved button, recommended apps);
Mission statement and logo with words ‘understanding and action’ prominently displayed
Sections
1. About WC - Who we are – Weightwise Commons Board and Research Steering Panel cvs; CEO and research officer – annual report
2. For General Public - The big questions about obesity – the interaction of food (protein & fructose), exercise, epigenetics “its not your fault”, hormones (eg leptin) & metabolism. The Fact Sheets; simple summaries of latest research?
3. For Professionals - Research Steering Panel - KPR Ebulletins - Research and Publications
4. Media and latest news on obesity
5. Support WC in its mission– get involved – note DGR status etc.
6. Website terms of use – Halbury to provide disclaimers etc
For later - professionals – Post Conference youtubes
- general public – anti-obesity app
Websites we like:
- http://www.sugarscalepro.com
- www.bellywellfund.org.au
- http://www.unaforce.org/international - clean lines; well organised
- http://www.verdantia.org/ good layout of tabs about us, news and media, science, login, myverdantpage
- http://www.stridequarter.co.uk/sport innovate way to promote fitness
We would also be keen to get the site coded so would like an estimate of how much it would cost to create the html version of the site also with css for the main styles.

```html
<!DOCTYPE html>
<html lang="en">
<head>
<meta charset="utf-8">
<title>Weightwise Commons – understanding and action</title>
<link href="https://fonts.googleapis.com/css2?family=Questrial&family=PT+Sans:wght@400;700&display=swap" rel="stylesheet">
<style>
:root{
  --teal:#12b5c9;
  --orange:#f0581a;
  --ink:#3a3a3a;
  --muted:#8c8c8c;
  --faint:#b9b9b9;
  --rule:#e4e4e4;
  --bg-top:#eaf0f9;
}
*{box-sizing:border-box;margin:0;padding:0}
html,body{width:1200px;height:866px;overflow:hidden}
body{
  position:relative;
  font-family:"PT Sans",sans-serif;
  color:var(--ink);
  background:linear-gradient(180deg,var(--bg-top) 0,#f5f8fc 140px,#ffffff 300px);
}
a{text-decoration:none;color:inherit}
.abs{position:absolute}

/* header */
.brand{left:108px;top:66px;width:205px;height:50px}
.brand-dot{position:absolute;left:0;top:6px;width:12px;height:12px;border-radius:50%;background:var(--teal)}
.brand-name{position:absolute;left:19px;top:0;font-weight:700;font-size:19px;line-height:24px;color:var(--teal);white-space:nowrap}
.brand-tag{position:absolute;left:19px;top:26px;font-size:12px;color:#888;white-space:nowrap}

.secure-login{left:700px;top:33px;font-size:12px;color:#666}
.secure-login::before{content:"";display:inline-block;border-left:4px solid var(--teal);border-top:3px solid transparent;border-bottom:3px solid transparent;margin-right:7px;vertical-align:1px}
.header-divider{left:806px;top:16px;width:1px;height:48px;background:linear-gradient(#fff0,#d6dbe3,#fff0)}
.search{left:841px;top:16px;width:243px;height:33px;background:#fff;border:1px solid #dde2ea;border-radius:5px}
.search-input{position:absolute;left:11px;top:8px;font-size:13px;color:#b5b5b5}
.search-btn{position:absolute;right:4px;top:5px;width:44px;height:21px;border-radius:4px;background:var(--teal);color:#fff;font-size:11px;text-align:center;line-height:21px}
.search-scopes{left:847px;top:55px;font-size:11px;color:#666;display:flex;gap:13px}
.search-scopes span::before{content:"";display:inline-block;width:7px;height:7px;border:1px solid #ccc;margin-right:5px;vertical-align:0}

.main-nav{left:325px;top:95px;width:754px;display:flex;justify-content:space-between;font-family:"Questrial",sans-serif;font-size:14px;color:#555}
.main-nav a{white-space:nowrap}
.main-nav .active{color:var(--teal)}
.header-rule{left:107px;top:130px;width:978px;height:1px;background:var(--rule)}

/* feature */
.feature{left:107px;top:131px;width:978px;height:340px;background:#fff;box-shadow:0 18px 28px -16px rgba(90,100,120,.18)}
.chart{position:absolute;left:0;top:0}
.chart-notes{left:140px;top:421px;font-size:11.5px;color:#888;line-height:15px}
.legend{left:638px;top:413px;font-size:11.5px;color:#888;line-height:14px}
.legend span{display:block}
.legend span::before{content:"";display:inline-block;width:9px;height:9px;margin-right:9px;vertical-align:-1px}
.legend .y95::before{background:var(--teal)}
.legend .y07::before{background:var(--orange)}

.feature-list{left:800px;top:155px;width:280px}
.feature-item{padding:8px 0 16px 32px;border-bottom:1px solid #ececec}
.feature-item.current{background:linear-gradient(90deg,#e9ebef 0,#fff 30px);padding-top:9px;height:104px}
.feature-item h3{font-family:"Questrial",sans-serif;font-weight:400;font-size:17px;line-height:22px;color:#666}
.feature-item.current h3{color:var(--teal)}
.feature-item p{font-size:13.5px;line-height:17px;color:var(--faint)}
.feature-item.current p{color:#999}
.feature-item.second{height:88px;padding-top:14px}
.feature-item.third{border-bottom:0;padding-top:8px}

/* columns */
.col h2{font-family:"Questrial",sans-serif;font-weight:400;font-size:22px;color:#333;padding-bottom:9px;border-bottom:4px solid #e6e6e6;margin-bottom:14px;white-space:nowrap}
.newsletter h2{font-size:20.5px;letter-spacing:-.3px}
.col p{font-size:13.5px;line-height:17px;color:#555}
.who{left:107px;top:518px;width:266px}
.who .more{display:block;color:var(--teal);font-size:13.5px;margin-top:1px}
.newsletter{left:450px;top:518px;width:283px}
.newsletter p{margin-top:18px}
.signup{margin-top:14px;width:277px;height:35px;border:1px solid #d8d8d8;border-radius:4px;position:relative}
.signup .field{position:absolute;left:15px;top:11px;font-size:11px;color:#aaa}
.signup .go{position:absolute;right:6px;top:6px;width:78px;height:22px;border-radius:4px;background:var(--teal);color:#fff;font-size:11px;text-align:center;line-height:22px}
.latest{left:810px;top:518px;width:275px}
.latest h4{font-size:13.5px;font-weight:400;line-height:17px;color:#222;margin-top:18px}
.latest .meta{font-size:10.5px;color:#777;margin-top:10px;line-height:13px}
.latest .meta a{color:var(--teal)}

/* footer */
.footer-rule{left:107px;top:700px;width:978px;height:1px;background:var(--rule)}
.social{left:0;top:722px;width:1200px;display:flex;justify-content:center;gap:22px;font-weight:700;font-size:15px;color:#9a9a9a}
.footer-nav{left:0;top:766px;width:1200px;text-align:center;font-size:11.5px;color:#444}
.footer-nav a{margin:0 4px}
.footer-nav .active{color:var(--teal)}
.footer-nav .dot{color:#aaa;margin:0 3px}
.copyright{left:0;top:786px;width:1200px;text-align:center;font-size:11px;color:#666}
</style>
</head>
<body>

<header>
  <a class="abs brand" href="#">
    <span class="brand-dot"></span>
    <span class="brand-name">Weightwise Commons</span>
    <span class="brand-tag">understanding and action</span>
  </a>
  <a class="abs secure-login" href="#">Secure Login</a>
  <div class="abs header-divider"></div>
  <form class="abs search">
    <span class="search-input">Search</span>
    <span class="search-btn">Search</span>
  </form>
  <div class="abs search-scopes"><span>Academic's Papers</span><span>Terms in fact sheets</span></div>
  <nav class="abs main-nav">
    <a href="#">About WC</a>
    <a href="#" class="active">For General Public</a>
    <a href="#">For Professionals</a>
    <a href="#">Latest News</a>
    <a href="#">Support WC</a>
    <a href="#">Terms of Use</a>
  </nav>
  <div class="abs header-rule"></div>
</header>

<section class="abs feature">
  <svg class="chart" width="700" height="340" viewBox="107 131 700 340" role="img" aria-label="Bar chart of proportion of people overweight or obese by age group, 1995 and 2007-08">
    <g font-family="PT Sans, sans-serif" fill="#888" font-size="11.5" font-weight="700">
      <text x="144" y="166">Percent (%)</text>
      <text x="446" y="396" text-anchor="middle">Age group (years)</text>
    </g>
    <g stroke="#dedede" stroke-width="1">
      <line x1="197" y1="193.5" x2="702" y2="193.5"/>
      <line x1="197" y1="233.5" x2="702" y2="233.5"/>
      <line x1="197" y1="272.5" x2="702" y2="272.5"/>
      <line x1="197" y1="312.5" x2="702" y2="312.5"/>
      <line x1="197" y1="352.5" x2="702" y2="352.5"/>
    </g>
    <g font-family="Questrial, sans-serif" font-size="15" fill="#222" text-anchor="end">
      <text x="179" y="196">80</text>
      <text x="179" y="236">60</text>
      <text x="179" y="276">40</text>
      <text x="179" y="316">20</text>
      <text x="179" y="355">0</text>
    </g>
    <g fill="var(--orange)">
      <rect x="270" y="239" width="14" height="113"/>
      <rect x="347" y="221" width="14" height="131"/>
      <rect x="422" y="215" width="14" height="137"/>
      <rect x="500" y="203" width="14" height="149"/>
      <rect x="576" y="195" width="14" height="157"/>
      <rect x="656" y="217" width="14" height="135"/>
    </g>
    <g fill="var(--teal)">
      <rect x="284" y="250" width="14" height="102"/>
      <rect x="361" y="233" width="14" height="119"/>
      <rect x="436" y="215" width="14" height="137"/>
      <rect x="514" y="209" width="14" height="143"/>
      <rect x="590" y="212" width="14" height="140"/>
      <rect x="670" y="222" width="14" height="130"/>
    </g>
    <g font-family="Questrial, sans-serif" font-size="14.5" fill="#222" text-anchor="middle">
      <text x="208" y="379">18-24</text>
      <text x="284" y="379">25-34</text>
      <text x="361" y="379">35-44</text>
      <text x="434" y="379">45-54</text>
      <text x="513" y="379">55-64</text>
      <text x="590" y="379">65-74</text>
      <text x="662" y="379">75 and over</text>
    </g>
  </svg>
</section>
<div class="abs chart-notes">(a) Measured Body Mass Index<br>(b) Excludes persons for whom measured height or weight was not available</div>
<div class="abs legend"><span class="y95">1995</span><span class="y07">2007-08</span></div>

<aside class="abs feature-list">
  <div class="feature-item current">
    <h3>3.5 Proportion of people overweight or obese by age</h3>
    <p>Source: National Nutrition Survey 1995 and National Health Survey 2007-08</p>
  </div>
  <div class="feature-item second">
    <h3>Research Steering Panel</h3>
    <p>Ut wisi enim ad minim veniam, quis nostrud exerci tation ullamcorper</p>
  </div>
  <div class="feature-item third">
    <h3>Research and Publications</h3>
    <p>Ut wisi enim ad minim veniam, quis nostrud exerci tation ullamcorper</p>
  </div>
</aside>

<section class="abs col who">
  <h2>Who We Are</h2>
  <p>Lorem ipsum dolor sit amet, consectetuer adipiscing elit, sed diam nonummy nibh euismod tincidunt ut laoreet dolore magna aliquam erat volutpat.</p>
  <a class="more" href="#">Read more</a>
</section>

<section class="abs col newsletter">
  <h2>Sign up for our e-newsletter!</h2>
  <p>Duis autem vel eum iriure dolor in hendrerit in vulputate velit esse molestie consequat</p>
  <form class="signup">
    <span class="field">Enter Email Address</span>
    <span class="go">Get Involved</span>
  </form>
</section>

<section class="abs col latest">
  <h2>Latest News</h2>
  <h4>Your Chance to ask EU President Marten Vos a question!</h4>
  <p class="meta">MAY, 4 2012<br>Posted by <a href="#">Daniel Prestwick</a></p>
</section>

<footer>
  <div class="abs footer-rule"></div>
  <div class="abs social"><a href="#">Chirpline</a><a href="#">Clipstream</a><a href="#">Friendgrid</a></div>
  <nav class="abs footer-nav">
    <a href="#">About WC</a><span class="dot">•</span>
    <a href="#" class="active">For General Public</a><span class="dot">•</span>
    <a href="#">For Professionals</a><span class="dot">•</span>
    <a href="#">Latest News</a><span class="dot">•</span>
    <a href="#">Support WC</a><span class="dot">•</span>
    <a href="#">Terms of Use</a>
  </nav>
  <p class="abs copyright">© 2011 Weightwise Commons. All right reserved</p>
</footer>

</body>
</html>
```